New Meal Prep Flyer for New Package Deals

We are looking for a design that displays our new packages that we offer. If you take a look at our website www.copperspoonpantry.com, and click on packages , you'll see the way we display them currently . We would like something similar to that in style . The first package is called "Evergreen" and this package will be a 1 week package (7 days ), 2 meals a day, for a price of $195.00. The second package is called "Pebble" and this package will be a 3 week package (21 days) 2 meals per day, for a price of $546.00 , the third package is a 6 week+ package (45 days), and it is called "Lighthouse" , 2 meals per day , and the price is $1080.00 .
For the Pebble Package , can you put next to it "Save $42.00!"
For the Lighthouse Package, can you put next to it "Save $180!"
We also want our logo on the flyer (see attached), and we are just looking for a 1 page flyer , 8 1/2 x 11.

```html
<!DOCTYPE html>
<html lang="en">
<head>
<meta charset="utf-8">
<title>Copper Spoon Pantry – Meal Prep Packages</title>
<link rel="stylesheet" href="https://fonts.googleapis.com/css2?family=Montserrat:wght@300;400;700;800;900&family=Oswald:wght@700&display=swap">
<style>
  :root {
    --orange: #f77f00;
    --orange-deep: #e86f00;
    --green: #8dc21f;
    --green-light: #a5cf3a;
    --green-deep: #5f9a17;
    --grey: #9d9d9d;
    --grey-light: #b3b3b3;
    --amber: #f5a623;
    --amber-light: #f7b733;
    --ink: #2b2b2b;
    --logo-grey: #7d7d7d;
    --paper: #ffffff;
    --sketch: #ececec;
    --gold: #d9a62c;
    --gold-light: #f3d27a;
  }
  * { box-sizing: border-box; margin: 0; padding: 0; }
  html, body { width: 800px; height: 1200px; overflow: hidden; background: var(--paper); }
  body { font-family: "Montserrat", sans-serif; position: relative; }

  .flyer { position: relative; width: 800px; height: 1200px; background: linear-gradient(160deg, #ffffff 0%, #f7f7f7 100%); overflow: hidden; }

  .art { position: absolute; }
  .art--board { left: 0; top: 0; width: 150px; height: 210px; background: linear-gradient(135deg, var(--sketch), #f6f6f6); border-bottom-right-radius: 90px; }
  .art--plate { right: 0; top: 0; width: 150px; height: 130px; background: radial-gradient(circle at 100% 0%, #e4e4e4 0%, #efefef 55%, rgba(255,255,255,0) 72%); }

  .brand { position: absolute; top: 78px; left: 0; width: 800px; text-align: center; }
  .brand__name { display: inline-flex; align-items: center; gap: 14px; font-weight: 800; font-size: 62px; letter-spacing: 3px; color: var(--logo-grey); line-height: 1; }
  .brand__dot { width: 22px; height: 22px; border-radius: 50%; background: var(--green); }
  .brand__tagline { margin-top: 16px; font-weight: 800; font-size: 26px; color: var(--green); letter-spacing: 0.2px; }
  .brand__tagline span { display: inline-block; margin: 0 12px; font-weight: 400; }

  .package { position: absolute; left: 62px; width: 674px; height: 248px; filter: drop-shadow(0 10px 8px rgba(0,0,0,0.18)); }
  .package--one { top: 233px; }
  .package--two { top: 529px; }
  .package--three { top: 827px; }

  .package__tab { position: absolute; left: 0; top: 0; width: 57px; height: 248px; border-radius: 22px 0 0 22px; }
  .package__tab-label { position: absolute; left: 50%; top: 50%; transform: translate(-50%, -50%) rotate(-90deg); color: #fff; font-weight: 800; font-size: 26px; white-space: nowrap; text-transform: uppercase; }

  .package__title { position: absolute; left: 57px; top: 0; width: 268px; height: 248px; padding: 44px 0 0 22px; }
  .package__weeks { font-weight: 900; font-size: 52px; line-height: 1; color: var(--ink); letter-spacing: -0.5px; }
  .package__word { font-weight: 800; font-size: 43px; line-height: 1.08; color: #fff; }
  .package__days { display: flex; align-items: center; gap: 10px; margin-top: 6px; color: #fff; font-weight: 400; font-size: 25px; }
  .package__days::before, .package__days::after { content: ""; width: 46px; height: 1.5px; background: rgba(255,255,255,0.85); }

  .package__meals { position: absolute; left: 325px; top: -9px; width: 201px; height: 266px; border-radius: 6px; }
  .package__meals-frame { position: absolute; left: 22px; top: 64px; width: 158px; height: 148px; border: 1.5px dashed rgba(0,0,0,0.55); border-radius: 4px; }
  .package__count { position: absolute; left: 50%; top: 36px; transform: translateX(-50%); width: 66px; height: 66px; border-radius: 50%; background: var(--ink); color: #fff; font-weight: 800; font-size: 44px; line-height: 66px; text-align: center; }
  .package__meals-text { position: absolute; left: 0; top: 112px; width: 100%; text-align: center; font-weight: 400; font-size: 37px; line-height: 1; }

  .package__fold { position: absolute; left: 526px; top: 0; width: 48px; height: 248px; border-radius: 14px 0 0 14px; }
  .package__price { position: absolute; left: 570px; top: 0; width: 104px; height: 248px; border-radius: 0 20px 20px 0; }
  .package__amount { position: absolute; left: 50%; top: 50%; transform: translate(-50%, -50%) rotate(-90deg); font-family: "Oswald", sans-serif; font-weight: 700; font-size: 64px; color: #fff; white-space: nowrap; letter-spacing: -1px; }
  .package__amount sup { font-size: 26px; vertical-align: 0; position: relative; top: 6px; margin-right: 2px; }

  .saving { position: absolute; width: 94px; height: 94px; border-radius: 50%; background: radial-gradient(circle at 35% 30%, var(--gold-light), var(--gold) 65%, #a8781a 100%); border: 4px solid #e9c465; box-shadow: 0 4px 8px rgba(0,0,0,0.3); text-align: center; color: var(--ink); font-family: "Oswald", sans-serif; font-weight: 700; transform: translate(-50%, -50%); z-index: 2; }
  .saving__label { display: block; margin-top: 14px; font-size: 15px; line-height: 1; }
  .saving__value { display: block; font-size: 36px; line-height: 1.05; }
  .saving__value sup { font-size: 15px; vertical-align: 0; position: relative; top: -14px; }
  .package--two .saving { left: 527px; top: 32px; }
  .package--three .saving { left: 540px; top: 44px; }

  /* colourways */
  .package--one .package__tab { background: var(--orange); }
  .package--one .package__title { background: linear-gradient(90deg, var(--green) 0%, var(--green-light) 100%); }
  .package--one .package__meals { background: var(--orange); }
  .package--one .package__meals-text { color: #fff; }
  .package--one .package__fold { background: linear-gradient(90deg, var(--green-deep), var(--green)); }
  .package--one .package__price { background: var(--grey); }

  .package--two .package__tab { background: var(--orange); }
  .package--two .package__title { background: linear-gradient(90deg, var(--grey) 0%, var(--grey-light) 100%); }
  .package--two .package__meals { background: var(--orange); }
  .package--two .package__meals-text { color: var(--ink); }
  .package--two .package__fold { background: linear-gradient(90deg, #888, var(--grey)); }
  .package--two .package__price { background: var(--green); }

  .package--three .package__tab { background: var(--green); }
  .package--three .package__title { background: linear-gradient(90deg, var(--amber) 0%, var(--amber-light) 100%); }
  .package--three .package__meals { background: var(--green); }
  .package--three .package__meals-text { color: var(--ink); }
  .package--three .package__fold { background: linear-gradient(90deg, var(--orange-deep), var(--orange)); }
  .package--three .package__price { background: var(--grey); }

  .site { position: absolute; left: 0; top: 1122px; width: 800px; display: flex; justify-content: center; align-items: center; gap: 14px; font-size: 25px; letter-spacing: 2.5px; color: var(--ink); }
  .site__domain { color: var(--green); font-weight: 700; }
  .site__dots { display: flex; gap: 7px; }
  .site__dots i { width: 8px; height: 8px; border-radius: 50%; background: var(--green); }
  .site__dots i:nth-child(1) { opacity: 0.45; }
  .site__dots i:nth-child(2) { opacity: 0.7; }
  .site__dots--end i:nth-child(1) { opacity: 1; }
  .site__dots--end i:nth-child(3) { opacity: 0.45; }
</style>
</head>
<body>
<main class="flyer">
  <div class="art art--board" role="img" aria-label="Line sketch of a chopping board with diced vegetables and herbs"></div>
  <div class="art art--plate" role="img" aria-label="Line sketch of a plate of pasta with vegetables"></div>

  <header class="brand">
    <div class="brand__name"><span class="brand__dot"></span>COPPER SPOON</div>
    <p class="brand__tagline">HEALTHY KITCHEN<span>|</span>MEAL PREP</p>
  </header>

  <section class="package package--one">
    <div class="package__tab"><span class="package__tab-label">Evergreen</span></div>
    <div class="package__title">
      <p class="package__weeks">1 WEEK</p>
      <p class="package__word">PACKAGE</p>
      <p class="package__days">(7 DAYS)</p>
    </div>
    <div class="package__meals">
      <div class="package__meals-frame"></div>
      <span class="package__count">2</span>
      <p class="package__meals-text">MEALS<br>A DAY</p>
    </div>
    <div class="package__fold"></div>
    <div class="package__price"><span class="package__amount"><sup>$</sup>195.00</span></div>
  </section>

  <section class="package package--two">
    <div class="package__tab"><span class="package__tab-label">Pebble</span></div>
    <div class="package__title">
      <p class="package__weeks">3 WEEK</p>
      <p class="package__word">PACKAGE</p>
      <p class="package__days">(21 DAYS)</p>
    </div>
    <div class="package__meals">
      <div class="package__meals-frame"></div>
      <span class="package__count">2</span>
      <p class="package__meals-text">MEALS<br>A DAY</p>
    </div>
    <div class="package__fold"></div>
    <div class="package__price"><span class="package__amount"><sup>$</sup>546.00</span></div>
    <div class="saving"><span class="saving__label">SAVE</span><span class="saving__value"><sup>$</sup>42</span></div>
  </section>

  <section class="package package--three">
    <div class="package__tab"><span class="package__tab-label">Lighthouse</span></div>
    <div class="package__title">
      <p class="package__weeks">6 WEEK</p>
      <p class="package__word">PACKAGE</p>
      <p class="package__days">(45 DAYS)</p>
    </div>
    <div class="package__meals">
      <div class="package__meals-frame"></div>
      <span class="package__count">2</span>
      <p class="package__meals-text">MEALS<br>A DAY</p>
    </div>
    <div class="package__fold"></div>
    <div class="package__price"><span class="package__amount"><sup>$</sup>1080.00</span></div>
    <div class="saving"><span class="saving__label">SAVE</span><span class="saving__value"><sup>$</sup>180</span></div>
  </section>

  <footer class="site">
    <span class="site__dots"><i></i><i></i><i></i></span>
    <span>www.<span class="site__domain">copperspoonpantry</span>.com</span>
    <span class="site__dots site__dots--end"><i></i><i></i><i></i></span>
  </footer>
</main>
</body>
</html>
```